Brisk Wire Services - Electrical

We need flyers for electrical services.
Areas of work include new builds, office fitouts, switchboard upgrades, installation of ceiling fans, powerpoint and downlight upgrades, home theatre and AV systems, all exterior and emergency work. Free quotes
We would like to see designs with the colour Red with a young and modern design. Licence No: 83146K must be included and call Leopold on 0418693027.

Colors
ec1f27

```html
<!DOCTYPE html>
<html lang="en">
<head>
<meta charset="utf-8">
<title>Brisk Wire Services – Electrical Flyer</title>
<link href="https://fonts.googleapis.com/css2?family=Oswald:wght@700&family=Open+Sans:wght@600;700;800&family=Signika:wght@600&family=Cinzel:wght@400;500&display=swap" rel="stylesheet">
<style>
  :root {
    --brand-red: #ec1f27;
    --band-red: #c8161d;
    --ink: #0c0c0c;
    --headline: #262626;
    --white: #ffffff;
    --badge: #e4dac8;
    --badge-edge: #c9bba3;
    --badge-text: #3a3a3a;
  }
  * { margin: 0; padding: 0; box-sizing: border-box; }
  html, body { width: 919px; height: 1200px; overflow: hidden; background: var(--ink); }
  .flyer {
    position: relative;
    width: 919px;
    height: 1200px;
    overflow: hidden;
    background: radial-gradient(ellipse at 40% 60%, #1c1c1c 0%, #0b0b0b 70%);
    font-family: "Open Sans", sans-serif;
    color: var(--white);
  }
  .hero { position: absolute; inset: 0 0 auto 0; width: 919px; height: 510px; }
  .headline {
    position: absolute;
    left: 0; right: 0; top: 30px;
    text-align: center;
    font-family: "Oswald", sans-serif;
    font-weight: 700;
    font-size: 80px;
    letter-spacing: 1px;
    color: var(--headline);
  }
  .tagline {
    position: absolute;
    left: 46px; top: 372px;
    transform-origin: left top;
    transform: rotate(5.6deg);
    font-weight: 700;
    font-size: 30px;
    white-space: nowrap;
    color: var(--white);
  }
  .areas-title {
    position: absolute;
    left: 56px; top: 478px;
    font-family: "Signika", sans-serif;
    font-weight: 600;
    font-size: 35px;
    color: var(--white);
  }
  .areas-underline { position: absolute; left: 54px; top: 522px; }
  .work-list {
    position: absolute;
    left: 62px; top: 558px;
    list-style: none;
  }
  .work-list li {
    display: flex;
    align-items: center;
    height: 37.6px;
    font-weight: 700;
    font-size: 23px;
  }
  .work-list svg { width: 24px; height: 24px; margin-right: 15px; flex: none; }
  .promise-badge {
    position: absolute;
    left: 573px; top: 560px;
    width: 292px; height: 258px;
    border-radius: 50%;
    background: radial-gradient(ellipse at 50% 45%, #ece3d3 0%, var(--badge) 60%, var(--badge-edge) 100%);
    display: flex;
    flex-direction: column;
    align-items: center;
    justify-content: center;
    color: var(--badge-text);
    font-weight: 700;
    font-size: 25px;
    line-height: 1.25;
    text-align: center;
  }
  .promise-badge hr {
    width: 210px;
    border: 0;
    border-top: 1px solid #b9ab93;
    margin: 8px 0;
  }
  .gallery {
    position: absolute;
    left: 45px; top: 862px;
    display: flex;
    gap: 8px;
  }
  .gallery-tile { width: 272px; height: 185px; border-radius: 7px; }
  .tile-fan { background: linear-gradient(135deg, #f2efe9 0%, #9c7a4e 45%, #c9ccd3 100%); }
  .tile-cables { background: linear-gradient(135deg, #ffffff 0%, #e9e7e2 40%, #5aa0d8 60%, #e8c63a 75%, #d94a3d 100%); }
  .tile-meter { background: linear-gradient(135deg, #ece4dc 0%, #c48f7a 35%, #4a80b8 65%, #d2d6d4 100%); }
  .call-line {
    position: absolute;
    left: 0; right: 0; top: 1074px;
    text-align: center;
    font-family: "Cinzel", serif;
    font-weight: 500;
    font-size: 37px;
    letter-spacing: 1px;
  }
  .call-line .phone { font-size: 48px; font-weight: 400; letter-spacing: 1px; }
  .footer-band {
    position: absolute;
    left: 0; bottom: 0;
    width: 919px; height: 57px;
    background: linear-gradient(180deg, var(--brand-red) 0%, var(--band-red) 100%);
    display: flex;
    align-items: center;
    justify-content: space-between;
    padding: 0 98px 0 37px;
  }
  .licence { font-size: 20px; letter-spacing: 2px; font-weight: 600; }
  .email { font-size: 27px; letter-spacing: 3px; font-weight: 800; }
</style>
</head>
<body>
<main class="flyer">
  <svg class="hero" viewBox="0 0 919 510" aria-hidden="false">
    <defs>
      <linearGradient id="heroTone" x1="0" y1="0" x2="1" y2="1">
        <stop offset="0" stop-color="#d9d6d2"/>
        <stop offset="0.35" stop-color="#d6b49c"/>
        <stop offset="0.6" stop-color="#8a8680"/>
        <stop offset="1" stop-color="#ecebe8"/>
      </linearGradient>
    </defs>
    <polygon role="img" aria-label="Photo of an electrician's hands wiring a wall junction box with a screwdriver"
             points="0,0 919,0 919,455 0,365" fill="url(#heroTone)"/>
    <polygon class="tag-band" points="0,362 919,452 919,505 0,424" fill="var(--brand-red)"/>
  </svg>

  <h1 class="headline">ELECTRICAL SERVICES</h1>
  <p class="tagline">Lorem ipsum dolor sit amet, consectetur adipiscing</p>

  <h2 class="areas-title">Areas of Work Include</h2>
  <svg class="areas-underline" width="386" height="10" viewBox="0 0 386 10" aria-hidden="true">
    <path d="M2 6 C80 3 200 4 384 3 L383 7 C220 8 90 8 3 9 Z" fill="var(--brand-red)"/>
  </svg>

  <ul class="work-list">
    <li><svg viewBox="0 0 24 24" aria-hidden="true"><circle cx="12" cy="12" r="11" fill="var(--brand-red)"/><circle cx="12" cy="12" r="7.5" fill="#fff"/><path d="M7 11.5 L11 15.5 L19 5" stroke="var(--brand-red)" stroke-width="3" fill="none" stroke-linecap="round"/></svg>New builds</li>
    <li><svg viewBox="0 0 24 24" aria-hidden="true"><circle cx="12" cy="12" r="11" fill="var(--brand-red)"/><circle cx="12" cy="12" r="7.5" fill="#fff"/><path d="M7 11.5 L11 15.5 L19 5" stroke="var(--brand-red)" stroke-width="3" fill="none" stroke-linecap="round"/></svg>Office Fitouts</li>
    <li><svg viewBox="0 0 24 24" aria-hidden="true"><circle cx="12" cy="12" r="11" fill="var(--brand-red)"/><circle cx="12" cy="12" r="7.5" fill="#fff"/><path d="M7 11.5 L11 15.5 L19 5" stroke="var(--brand-red)" stroke-width="3" fill="none" stroke-linecap="round"/></svg>Switchboard upgrades</li>
    <li><svg viewBox="0 0 24 24" aria-hidden="true"><circle cx="12" cy="12" r="11" fill="var(--brand-red)"/><circle cx="12" cy="12" r="7.5" fill="#fff"/><path d="M7 11.5 L11 15.5 L19 5" stroke="var(--brand-red)" stroke-width="3" fill="none" stroke-linecap="round"/></svg>Installation of ceiling fans</li>
    <li><svg viewBox="0 0 24 24" aria-hidden="true"><circle cx="12" cy="12" r="11" fill="var(--brand-red)"/><circle cx="12" cy="12" r="7.5" fill="#fff"/><path d="M7 11.5 L11 15.5 L19 5" stroke="var(--brand-red)" stroke-width="3" fill="none" stroke-linecap="round"/></svg>Powerpoint and downlight upgrades</li>
    <li><svg viewBox="0 0 24 24" aria-hidden="true"><circle cx="12" cy="12" r="11" fill="var(--brand-red)"/><circle cx="12" cy="12" r="7.5" fill="#fff"/><path d="M7 11.5 L11 15.5 L19 5" stroke="var(--brand-red)" stroke-width="3" fill="none" stroke-linecap="round"/></svg>Home theatre and AV systems</li>
    <li><svg viewBox="0 0 24 24" aria-hidden="true"><circle cx="12" cy="12" r="11" fill="var(--brand-red)"/><circle cx="12" cy="12" r="7.5" fill="#fff"/><path d="M7 11.5 L11 15.5 L19 5" stroke="var(--brand-red)" stroke-width="3" fill="none" stroke-linecap="round"/></svg>All exterior and emergency work</li>
  </ul>

  <aside class="promise-badge">
    <span>FREE QUOTES<br>AVAILABLE</span>
    <hr>
    <span>GUARANTEED</span>
    <hr>
    <span>SATISFACTION</span>
  </aside>

  <section class="gallery">
    <div class="gallery-tile tile-fan" role="img" aria-label="Photo of an electrician installing a ceiling fan"></div>
    <div class="gallery-tile tile-cables" role="img" aria-label="Photo of coloured electrical cables on a wiring plan"></div>
    <div class="gallery-tile tile-meter" role="img" aria-label="Photo of a multimeter testing a switchboard"></div>
  </section>

  <p class="call-line">CALL LEOPOLD ON : <span class="phone">0418693027</span></p>

  <footer class="footer-band">
    <span class="licence">Licence No: 83146K</span>
    <span class="email">info@briskwire.net</span>
  </footer>
</main>
</body>
</html>
```